Business card for Property Management consultant

I need a business card for my business LX Vantage - I consult to real estate agents to improve the performance of their Property Management departments (rental houses management). The card needs to be very professional looking, incorporating our logo and my photo plus the line "Develop your Rent Roll to Perform"

Target Market(s)

Real Estate business owners

Industry/Entity Type

Business Consultant

Contact Information for Business Card

Business name - LX Vantage (logo uploaded)
My Name : Marcia Kellaway -
Title : Property Management Consultant

Develop your Rent Roll to perform

Phone : +61 438592716
email : marcia@lxvantage.com.au
website ; www.lxvantage.com.au

Requirements
Must have
• Logo
• My photo
• Very corporate / professional look

```html
<!DOCTYPE html>
<html lang="en">
<head>
<meta charset="utf-8">
<title>LX Vantage – Business Card</title>
<link href="https://fonts.googleapis.com/css2?family=Montserrat:wght@500;600&family=Roboto+Condensed:wght@400&family=Didact+Gothic&display=swap" rel="stylesheet">
<style>
  :root {
    --stage: #0b0b0c;
    --card-black: #040405;
    --card-grey: #3b3c3e;
    --brand-blue: #3f72c9;
    --sky-blue: #3aa6e0;
    --gold: #d79a2b;
    --white: #f4f4f4;
    --soft-white: #dcdcdc;
  }
  * { margin: 0; padding: 0; box-sizing: border-box; }
  html, body {
    width: 1200px; height: 1120px; overflow: hidden;
    background: var(--stage);
  }
  .canvas {
    position: relative; width: 1200px; height: 1120px;
  }
  .card {
    position: absolute; left: 100px; top: 274px;
    width: 1000px; height: 572px; overflow: hidden;
    background: var(--card-black);
  }
  .card__shade {
    position: absolute; inset: 0;
    background: linear-gradient(118deg, transparent 0 52%, #1a1a1c 64%, var(--card-grey) 100%);
  }
  .card__photo {
    position: absolute; left: 70px; top: 40px; width: 470px; height: 532px;
    background:
      radial-gradient(ellipse 38% 34% at 48% 30%, #6b3a28 0%, #3a2017 55%, transparent 75%),
      radial-gradient(ellipse 70% 40% at 45% 100%, #2f5fcf 0%, #2a56bd 60%, transparent 80%),
      var(--card-black);
  }
  .card__band {
    position: absolute; left: 0; right: 0; bottom: 0; height: 12px;
    background: var(--brand-blue);
  }
  .brand {
    position: absolute; left: 580px; top: 54px; width: 380px;
  }
  .brand__row { display: flex; align-items: center; gap: 14px; }
  .brand__mark { width: 26px; height: 26px; background: var(--sky-blue); }
  .brand__name {
    font-family: "Montserrat", sans-serif; font-weight: 600;
    font-size: 46px; color: var(--white); letter-spacing: 1px;
  }
  .brand__rule {
    height: 2px; background: var(--brand-blue); margin: 10px 0 8px 40px;
  }
  .brand__tagline {
    font-family: "Montserrat", sans-serif; font-weight: 600;
    font-size: 17px; color: var(--white); letter-spacing: 1.5px;
    text-align: right;
  }
  .brand__role {
    font-family: "Didact Gothic", sans-serif; font-size: 18px;
    color: var(--soft-white); letter-spacing: 1px; text-align: right; margin-top: 4px;
  }
  .person { position: absolute; left: 580px; top: 224px; width: 380px; text-align: right; }
  .person__name {
    font-family: "Roboto Condensed", sans-serif; font-size: 44px; color: var(--gold);
  }
  .person__motto {
    font-family: "Didact Gothic", sans-serif; font-size: 17px;
    color: var(--white); letter-spacing: 1px;
  }
  .contact {
    position: absolute; right: 40px; top: 372px; text-align: right;
    font-family: "Didact Gothic", sans-serif; color: var(--white);
  }
  .contact__phone {
    font-family: "Montserrat", sans-serif; font-weight: 600;
    font-size: 30px; color: var(--sky-blue); margin-bottom: 6px;
  }
  .contact__line { font-size: 22px; letter-spacing: 1.5px; line-height: 1.35; }
</style>
</head>
<body>
<main class="canvas">
  <section class="card">
    <div class="card__shade"></div>
    <div class="card__photo" role="img" aria-label="Portrait photo of Marcia Kellaway in a blue jacket on a black background"></div>

    <header class="brand">
      <div class="brand__row">
        <span class="brand__mark"></span>
        <span class="brand__name">LX Vantage</span>
      </div>
      <div class="brand__rule"></div>
      <p class="brand__tagline">STRATEGY - GROWTH - PROFIT</p>
      <p class="brand__role">Property Management Consultant</p>
    </header>

    <div class="person">
      <h1 class="person__name">Marcia Kellaway</h1>
      <p class="person__motto">Develop Your Rent Roll to perform</p>
    </div>

    <address class="contact" style="font-style: normal;">
      <p class="contact__phone">+61 438592716</p>
      <p class="contact__line">marcia@lxvantage.com.au</p>
      <p class="contact__line">www.lxvantage.com.au</p>
    </address>

    <div class="card__band"></div>
  </section>
</main>
</body>
</html>
```